Re make of the website. A fine diamond jeweller based in Melbourne Australia.

We would like the website redesigned. http://hollisfenwick.com.au/

Current website is very dated and we would like it re made and updated. An example of what we would like is https://www.taryndulcette.com/au/ or https://brindlecove.co.nz/

We sell high end diamond jewellery and the main purpose of the website will be to get people to enquire and make a booking to design a ring/meet with the experts in store. There is also a small online store.

Target Market(s)

High Affluence 25-70

Number of Pages Required

5+ page

Font styles to use
Sans Serif
Other font styles liked:
• Muli Fine

Requirements
Must have
• All the current features on the website
• Very elegant
• Main cover image
• Lots of lifestyle imagers - less blank space
• 1. Online Shop
• 2. Home page
• 3. Contact us/enquiry page
• 4. Jewellery Page
• 5. About page

```html
<!DOCTYPE html>
<html lang="en">
<head>
<meta charset="utf-8">
<title>Hollis Fenwick — Shop</title>
<link href="https://fonts.googleapis.com/css2?family=Mulish:wght@400;600;700&display=swap" rel="stylesheet">
<style>
  :root {
    --ink: #1a1a1a;
    --text: #333333;
    --muted: #5a5a5a;
    --page: #f4f4f4;
    --white: #ffffff;
    --rule: #222222;
    --soft-rule: #8a8a8a;
    --heart: #f26d6d;
    --photo-a: #ffffff;
    --photo-b: #e6e6e6;
  }
  * { box-sizing: border-box; margin: 0; padding: 0; }
  html, body { width: 1200px; height: 1200px; overflow: hidden; }
  body {
    position: relative;
    background: var(--page);
    font-family: "Mulish", sans-serif;
    color: var(--text);
  }
  .site-header { position: absolute; left: 0; top: 0; width: 1200px; height: 173px; background: var(--white); }
  .utility-bar { position: absolute; left: 14px; right: 14px; top: 0; height: 52px; border-bottom: 2px solid var(--rule); display: flex; align-items: center; font-size: 16px; color: var(--muted); }
  .utility-bar span { display: inline-flex; align-items: center; gap: 8px; margin-right: 45px; }
  .utility-bar .cart { margin-left: auto; margin-right: 0; }
  .utility-bar svg { stroke: #9a9a9a; fill: none; stroke-width: 1.4; }
  .brand { position: absolute; left: 15px; top: 65px; display: flex; align-items: flex-end; gap: 9px; }
  .brand-square { width: 86px; height: 86px; background: var(--ink); }
  .brand-name { font-size: 34px; font-weight: 400; color: var(--ink); letter-spacing: 1px; line-height: 1; margin-bottom: 2px; }
  .search { position: absolute; left: 1162px; top: 78px; stroke: #8a8a8a; fill: none; stroke-width: 2.4; }
  .main-nav { position: absolute; top: 134px; left: 0; font-size: 16px; letter-spacing: 1.3px; color: var(--text); }
  .main-nav a { position: absolute; white-space: nowrap; text-decoration: none; color: inherit; }
  .breadcrumb { position: absolute; right: 20px; top: 189px; font-size: 12px; color: var(--ink); }
  .breadcrumb .dot { margin: 0 10px; }
  .page-title { position: absolute; left: 0; width: 1200px; top: 219px; text-align: center; font-size: 26px; font-weight: 400; letter-spacing: 1px; color: var(--ink); }
  .filters { position: absolute; left: 83px; top: 277px; width: 1035px; border-top: 1px solid var(--rule); }
  .filter { position: absolute; top: 0; height: 43px; width: 323px; border-bottom: 1px solid var(--rule); display: flex; align-items: center; padding-left: 22px; gap: 14px; font-size: 16px; letter-spacing: 1.5px; color: var(--ink); }
  .filter svg { stroke: var(--ink); fill: none; stroke-width: 2; }
  .card { position: absolute; width: 315px; height: 507px; background: var(--white); box-shadow: 0 1px 4px rgba(0,0,0,0.08); }
  .product-photo { position: absolute; left: 54px; top: 24px; width: 216px; height: 208px; background: radial-gradient(circle at 50% 55%, var(--photo-a), var(--photo-b)); }
  .wish { position: absolute; left: 258px; top: 199px; width: 28px; height: 28px; border: 1px solid #9a9a9a; background: var(--white); display: flex; align-items: center; justify-content: center; }
  .wish svg { stroke: #9a9a9a; fill: none; stroke-width: 1.4; }
  .wish.is-saved svg { fill: var(--heart); stroke: var(--heart); }
  .product-name { position: absolute; left: 0; width: 100%; top: 260px; text-align: center; font-size: 19.5px; font-weight: 700; letter-spacing: 1px; color: var(--ink); }
  .product-desc { position: absolute; left: 33px; width: 252px; top: 306px; height: 91px; border-top: 1px solid var(--soft-rule); border-bottom: 1px solid var(--soft-rule); padding-top: 6px; font-size: 14.5px; line-height: 25px; letter-spacing: 1px; color: var(--muted); text-align: justify; }
  .add-to-cart { position: absolute; left: 78px; top: 429px; width: 159px; height: 46px; border: 2px solid var(--ink); display: flex; align-items: center; justify-content: center; font-size: 15px; letter-spacing: 1.5px; color: var(--ink); }
</style>
</head>
<body>
<header class="site-header">
  <div class="utility-bar">
    <span>My Wish List <svg width="20" height="18" viewBox="0 0 20 18"><path d="M10 16.5 2.5 9A4.3 4.3 0 0 1 10 3.5 4.3 4.3 0 0 1 17.5 9Z"/></svg></span>
    <span>Sign In</span>
    <span>Create an Account <svg width="18" height="18" viewBox="0 0 18 18"><circle cx="9" cy="6" r="4.2"/><path d="M1.5 17.5c1-4 4-5.5 7.5-5.5s6.5 1.5 7.5 5.5"/></svg></span>
    <span class="cart">Cart(0) <svg width="22" height="24" viewBox="0 0 22 24"><rect x="2" y="7" width="18" height="16"/><path d="M7 10V5a4 4 0 0 1 8 0v5"/></svg></span>
  </div>
  <div class="brand">
    <div class="brand-square"></div>
    <div class="brand-name">HOLLIS FENWICK</div>
  </div>
  <svg class="search" width="26" height="26" viewBox="0 0 26 26"><circle cx="10.5" cy="10.5" r="8.5"/><path d="M17 17l7 7"/></svg>
  <nav class="main-nav">
    <a style="left:591px">HOME</a>
    <a style="left:689px">SHOP</a>
    <a style="left:785px">COLLECTION</a>
    <a style="left:940px">ABOUT HF</a>
    <a style="left:1077px">CONTACT US</a>
  </nav>
</header>

<div class="breadcrumb">Home<span class="dot">•</span>Shop</div>
<h1 class="page-title">PRODUCTS</h1>

<div class="filters">
  <div class="filter" style="left:0"><svg width="14" height="9" viewBox="0 0 14 9"><path d="M1 1l6 6 6-6"/></svg>Categories</div>
  <div class="filter" style="left:355px"><svg width="14" height="9" viewBox="0 0 14 9"><path d="M1 1l6 6 6-6"/></svg>Sort by</div>
  <div class="filter" style="left:711px"><svg width="14" height="9" viewBox="0 0 14 9"><path d="M1 1l6 6 6-6"/></svg>Dispaly</div>
</div>

<article class="card" style="left:86px;top:388px">
  <div class="product-photo" role="img" aria-label="Product photo: white gold bar necklace set with diamonds"></div>
  <div class="wish is-saved"><svg width="18" height="16" viewBox="0 0 20 18"><path d="M10 16.5 2.5 9A4.3 4.3 0 0 1 10 3.5 4.3 4.3 0 0 1 17.5 9Z"/></svg></div>
  <h2 class="product-name">Geometric Bar Necklace</h2>
  <p class="product-desc">Hollis Collection geometric bar necklace with 35 diamonds in 18 carat white gold</p>
  <div class="add-to-cart">ADD TO CART</div>
</article>
<article class="card" style="left:442px;top:388px">
  <div class="product-photo" role="img" aria-label="Product photo: white gold bar necklace set with diamonds"></div>
  <div class="wish"><svg width="18" height="16" viewBox="0 0 20 18"><path d="M10 16.5 2.5 9A4.3 4.3 0 0 1 10 3.5 4.3 4.3 0 0 1 17.5 9Z"/></svg></div>
  <h2 class="product-name">Geometric Bar Necklace</h2>
  <p class="product-desc">Hollis Collection geometric bar necklace with 35 diamonds in 18 carat white gold</p>
  <div class="add-to-cart">ADD TO CART</div>
</article>
<article class="card" style="left:802px;top:388px">
  <div class="product-photo" role="img" aria-label="Product photo: white gold bar necklace set with diamonds"></div>
  <div class="wish"><svg width="18" height="16" viewBox="0 0 20 18"><path d="M10 16.5 2.5 9A4.3 4.3 0 0 1 10 3.5 4.3 4.3 0 0 1 17.5 9Z"/></svg></div>
  <h2 class="product-name">Geometric Bar Necklace</h2>
  <p class="product-desc">Hollis Collection geometric bar necklace with 35 diamonds in 18 carat white gold</p>
  <div class="add-to-cart">ADD TO CART</div>
</article>

<article class="card" style="left:86px;top:956px">
  <div class="product-photo" role="img" aria-label="Product photo: white gold bar necklace set with diamonds"></div>
  <div class="wish"><svg width="18" height="16" viewBox="0 0 20 18"><path d="M10 16.5 2.5 9A4.3 4.3 0 0 1 10 3.5 4.3 4.3 0 0 1 17.5 9Z"/></svg></div>
</article>
<article class="card" style="left:442px;top:956px">
  <div class="product-photo" role="img" aria-label="Product photo: white gold bar necklace set with diamonds"></div>
  <div class="wish"><svg width="18" height="16" viewBox="0 0 20 18"><path d="M10 16.5 2.5 9A4.3 4.3 0 0 1 10 3.5 4.3 4.3 0 0 1 17.5 9Z"/></svg></div>
</article>
<article class="card" style="left:802px;top:956px">
  <div class="product-photo" role="img" aria-label="Product photo: white gold bar necklace set with diamonds"></div>
  <div class="wish"><svg width="18" height="16" viewBox="0 0 20 18"><path d="M10 16.5 2.5 9A4.3 4.3 0 0 1 10 3.5 4.3 4.3 0 0 1 17.5 9Z"/></svg></div>
</article>
</body>
</html>
```